New Packaging and label for New Beard Oil and Shampoo brand from London

Oils, Shampoo ect .. Beard Oil Ingredients: Application Directions: Apply to beard by weight in a small amount of oil will naturally absorb. Leaving it soft & conditioned. Ingredients: Coconut oil, scented oil, Oud oil, vitamin E 100% Natural `i will have 5 types of oils Vanilla Oud Rose Oud Cocktail Tea tree Arabian Night

Target Market(s)

A fashionable well groomed professional gentleman who is willing to invest in his appearance.

Industry/Entity Type

It Company

Font styles to use
Sans Serif

Colors

Designer to choose colors to be used in the design.

Requirements
Must have
• Beard Oil Ingredients: Application Directions: Apply to a beard by a small amount of oil will naturally absorb. Leaving it soft & conditioned. Ingredients: Coconut Oil, Scented Oil, Oil Oud, Vitamin E 100% Natural 1.0z 30ml Made in Uk i will have 5 types of oils Vanilla Oud Rose Oud Cocktail Tea Tree Arabian Beard Night Shampoo APPLICATION DIRECTIONS Massage into the beard / hair and rinse out with warm water. Distorted shampoos, there are no nasty chemicals which are damaging your beard instead of the wheat proteins and oils that you add to the hair follicles with nutrients and naturally adding a protective coating. INGREDIENTS Aqua (Water), Capryl / caprylyl glucoside, Cocomidopropyl betaine, Glycerin (Veg), Xanthan gum, Phenoxyethanol, Hydrolysed wheat protein, Aloe barbadensis (Aloe vera) leaf powder, Sodium benzoate, Potassium sorbate1 3.4 oz, 100ml Cylinder packaging for the Oils, Box for the shampoo
Nice to have
• I want "London" written underneath the logo and oil name.

```html
<!DOCTYPE html>
<html lang="en">
<head>
<meta charset="utf-8">
<title>Harrow &amp; Vale – Tea Tree Beard Shampoo Labels</title>
<link rel="stylesheet" href="https://fonts.googleapis.com/css2?family=Montserrat:wght@400;500;600;700&display=swap">
<style>
  :root {
    --page: #ffffff;
    --label-light: #f4f4f4;
    --label-dark: #111111;
    --ink-dark: #2a2a2a;
    --ink-light: #f2f2f2;
    --ink-muted-light: #6a6a6a;
    --ink-muted-dark: #b9b9b9;
    --gold: #c9a14a;
    --stripe-dark: #7a7a7a;
    --stripe-light: #9a9a9a;
  }
  * { box-sizing: border-box; margin: 0; padding: 0; }
  html, body {
    width: 1200px; height: 771px; overflow: hidden;
    background: var(--page);
    font-family: "Montserrat", sans-serif;
  }
  .canvas { position: relative; width: 1200px; height: 771px; }

  .label {
    position: absolute; top: 110px; width: 320px; height: 600px;
    border-radius: 28px;
    display: flex; flex-direction: column; align-items: center;
    text-align: center;
  }
  .label--front-light { left: 56px;  background: var(--label-light); color: var(--ink-dark); box-shadow: inset 0 0 0 1px #e2e2e2; }
  .label--front-dark  { left: 418px; background: var(--label-dark);  color: var(--ink-light); }
  .label--back-dark   { left: 817px; background: var(--label-dark);  color: var(--ink-light); }

  .stripe-band { width: 76px; height: 26px; }
  .label--front-light .stripe-band { background: var(--stripe-light); }
  .label--front-dark .stripe-band,
  .label--back-dark .stripe-band { background: var(--stripe-dark); }
  .stripe-band--top { margin-top: 235px; }
  .stripe-band--bottom { margin-top: 14px; }

  .brand-name {
    margin-top: 30px;
    font-weight: 700; font-size: 15px; letter-spacing: 1px;
    text-transform: uppercase;
  }
  .product-name {
    margin-top: 30px;
    font-weight: 500; font-size: 30px; letter-spacing: 2px;
    color: var(--gold);
  }
  .product-type {
    margin-top: 6px;
    font-size: 9px; letter-spacing: 1.5px; text-transform: uppercase;
  }
  .label--front-light .product-type,
  .label--front-light .origin { color: var(--ink-muted-light); }
  .label--front-dark .product-type,
  .label--front-dark .origin { color: var(--ink-muted-dark); }
  .origin {
    margin-top: 66px;
    font-size: 7px; letter-spacing: 1px; text-transform: uppercase;
  }

  .back-copy { width: 250px; margin-top: 278px; }
  .back-heading {
    font-size: 7.5px; font-weight: 600; letter-spacing: 1px;
    text-transform: uppercase; margin-bottom: 5px;
  }
  .back-text {
    font-size: 7px; line-height: 1.55; color: var(--ink-muted-dark);
    margin-bottom: 10px;
  }
  .made-in {
    margin-top: 24px; font-size: 7px; font-weight: 600; letter-spacing: 1px;
    color: var(--gold); text-transform: uppercase;
  }
  .volume { margin-top: 18px; font-size: 7px; letter-spacing: 0.5px; color: var(--ink-muted-dark); }
  .label--back-dark .stripe-band--top { position: absolute; top: 235px; margin: 0; }
</style>
</head>
<body>
<main class="canvas">

  <section class="label label--front-light">
    <div class="stripe-band stripe-band--top" role="img" aria-label="Decorative vertical line pattern"></div>
    <div class="brand-name">Harrow &amp; Vale</div>
    <div class="product-name">[TEA TREE]</div>
    <div class="product-type">Beard Shampoo</div>
    <div class="origin">London</div>
    <div class="stripe-band stripe-band--bottom" role="img" aria-label="Decorative vertical line pattern"></div>
  </section>

  <section class="label label--front-dark">
    <div class="stripe-band stripe-band--top" role="img" aria-label="Decorative vertical line pattern"></div>
    <div class="brand-name">Harrow &amp; Vale</div>
    <div class="product-name">[TEA TREE]</div>
    <div class="product-type">Beard Shampoo</div>
    <div class="origin">London</div>
    <div class="stripe-band stripe-band--bottom" role="img" aria-label="Decorative vertical line pattern"></div>
  </section>

  <section class="label label--back-dark">
    <div class="stripe-band stripe-band--top" role="img" aria-label="Decorative vertical line pattern"></div>
    <div class="back-copy">
      <h2 class="back-heading">Application Directions</h2>
      <p class="back-text">Massage into the beard / hair and rinse out with warm water. Unlike conventional shampoos, there are no nasty chemicals which are damaging your beard; instead the wheat proteins and oils feed the hair follicles with nutrients and naturally add a protective coating.</p>
      <h2 class="back-heading">Ingredients</h2>
      <p class="back-text">Aqua (Water), Capryl / caprylyl glucoside, Cocamidopropyl betaine, Glycerin (Veg), Xanthan gum, Phenoxyethanol, Hydrolysed wheat protein, Aloe barbadensis (Aloe vera) leaf powder, Sodium benzoate, Potassium sorbate.</p>
      <p class="made-in">Made in the UK</p>
      <p class="volume">3.4 oz · 100ml</p>
    </div>
  </section>

</main>
</body>
</html>
```